New ante natal classes need competitive poster design

I am starting a new independent childbirth preparation business. There is a lot of competition from "trendy" practitioners locally. As an older and experienced childbirth educator I need to have a different appeal and image - That of experience/wisdom/grandmotherliness whilst being up to date with latest thinking . I am a mother of four and grandmother and have prepared over 1000 women for birth. The design needs to give a modern take on tradition with a mother and baby context. The name of my business is "willow cradle", the poster will need to be sufficiently different to stand out on any notice board. Text as follows:
willow cradle
Birth and parenthood classes using the most effective preparation techniques run by experienced PBG teacher/trainer
Classes cover:
choices in childbirth
normal pregnancy, labour and variations
self help techniques for labour including hypno-birthing
breastfeeding
baby care and paediatric first aid

Call 07481236590

Industry/Entity Type

Business

```html
<!DOCTYPE html>
<html lang="en">
<head>
<meta charset="utf-8">
<title>Willow Cradle – Birth and Parenthood Classes</title>
<link rel="stylesheet" href="https://fonts.googleapis.com/css2?family=Bebas+Neue&display=swap">
<style>
  :root {
    --sky: #c3cfd3;
    --blush: #cfb6bb;
    --berry: #874a4e;
    --berry-soft: #a5838a;
    --white: #ffffff;
    --ink: #2f2f31;
    --photo-light: #e4dfe0;
    --photo-mid: #b89ea3;
    --photo-deep: #7f5a5f;
  }
  * { margin: 0; padding: 0; box-sizing: border-box; }
  html, body { width: 848px; height: 1200px; overflow: hidden; }
  body { font-family: "Bebas Neue", "Arial Narrow", sans-serif; }

  .poster {
    position: relative;
    width: 848px;
    height: 1200px;
    background: linear-gradient(180deg, var(--sky) 0%, #c8ced2 45%, var(--blush) 100%);
    overflow: hidden;
  }
  .poster-frame {
    position: absolute;
    inset: 12px;
    border: 1.5px solid rgba(255,255,255,0.85);
    pointer-events: none;
  }

  .brand-title {
    position: absolute;
    top: 60px; left: 0; right: 0;
    text-align: center;
    white-space: nowrap;
    color: var(--berry);
    font-size: 126px;
    line-height: 1;
    letter-spacing: 3px;
    font-weight: 400;
  }

  .tagline {
    position: absolute;
    top: 226px; left: 0; right: 0;
    text-align: center;
    white-space: nowrap;
    color: var(--white);
    font-size: 31px;
    line-height: 33px;
    letter-spacing: 0.3px;
  }

  .rule-double {
    position: absolute;
    left: 48px; right: 48px;
    height: 6px;
    border-top: 1.5px solid var(--white);
    border-bottom: 1.5px solid var(--white);
  }
  .rule-top { top: 304px; }
  .rule-bottom { top: 934px; }

  .hero-photo {
    position: absolute;
    left: 262px; top: 312px;
    width: 578px; height: 620px;
    background:
      radial-gradient(ellipse 40% 45% at 30% 58%, var(--photo-light) 0%, rgba(228,223,224,0) 100%),
      radial-gradient(ellipse 55% 60% at 70% 40%, var(--photo-deep) 0%, var(--photo-mid) 55%, rgba(184,158,163,0) 100%);
    -webkit-mask-image: linear-gradient(90deg, transparent 0%, #000 18%, #000 100%);
    mask-image: linear-gradient(90deg, transparent 0%, #000 18%, #000 100%);
  }

  .call-badge {
    position: absolute;
    left: 47px; top: 360px;
    width: 204px; height: 204px;
    border-radius: 50%;
    background: #e6e9ea;
    border: 2px solid var(--ink);
    box-shadow: inset 0 0 0 8px #e6e9ea, inset 0 0 0 9px rgba(47,47,49,0.25);
  }
  .call-badge svg {
    position: absolute;
    left: 50%; top: 30px;
    transform: translateX(-50%);
  }
  .call-number {
    position: absolute;
    left: 0; right: 0; top: 108px;
    text-align: center;
    white-space: nowrap;
    color: var(--ink);
    font-size: 42px;
    letter-spacing: -0.5px;
  }

  .classes-heading {
    position: absolute;
    top: 954px; left: 0; right: 0;
    text-align: center;
    color: var(--berry);
    font-size: 30px;
    letter-spacing: 0.5px;
  }
  .classes-heading span {
    border-bottom: 2px solid var(--berry);
    padding-bottom: 1px;
  }

  .classes-list {
    position: absolute;
    left: 146px; top: 993px;
    width: 560px; height: 166px;
    background: var(--berry-soft);
    border: 1.5px solid var(--white);
    list-style: none;
    padding-top: 13px;
    text-align: center;
    color: var(--white);
    font-size: 22px;
    line-height: 24px;
  }
</style>
</head>
<body>
  <main class="poster">
    <div class="poster-frame"></div>

    <h1 class="brand-title">WILLOW CRADLE</h1>

    <p class="tagline">
      BIRTH AND PARENTHOOD CLASSES USING THE MOST EFFECTIVE<br>
      PREPARATION TECHNIQUES RUN BY EXPERIENCED PBG TEACHER / TRAINER
    </p>

    <div class="rule-double rule-top"></div>

    <div class="hero-photo" role="img" aria-label="Photograph of a mother kissing her baby on the head"></div>

    <div class="call-badge">
      <svg width="92" height="70" viewBox="0 0 92 70" aria-hidden="true">
        <path d="M8 18 C8 6 84 6 84 18 L80 26 L64 24 L62 16 C54 13 38 13 30 16 L28 24 L12 26 Z" fill="#3a3a3c"/>
        <path d="M28 26 L64 26 L76 58 C76 62 74 64 70 64 L22 64 C18 64 16 62 16 58 Z" fill="#3a3a3c"/>
        <circle cx="46" cy="44" r="13" fill="#8d8d90"/>
        <circle cx="46" cy="44" r="5" fill="#3a3a3c"/>
      </svg>
      <div class="call-number">07481236590</div>
    </div>

    <div class="rule-double rule-bottom"></div>

    <h2 class="classes-heading"><span>CLASSES COVER:</span></h2>

    <ul class="classes-list">
      <li>CHOICES IN CHILDBIRTH</li>
      <li>NORMAL PREGNANCY</li>
      <li>LABOUR AND VARIATIONS</li>
      <li>SELF HELP TECHNIQUES FOR LABOUR INCLUDING HYPNO-BIRTHING</li>
      <li>BREASTFEEDING</li>
      <li>BABY CARE AND PAEDIATRIC FIRST AID</li>
    </ul>
  </main>
</body>
</html>
```